Website for Apartment Rental in Prague

I would like to create designs of my website focused on luxury apartment rentals in Prague, Czech Republic. I created initial mock-ups, They are all attached. I need to design homepage and subpage. The mock-ups were created by combining elements from different websites that I liked but I need you to create a design that is unique and original. The attached files a only a guidance for the structure of the website but not for the design. Try to be creative.

Industry/Entity Type

Apartment

```html
<!DOCTYPE html>
<html lang="en">
<head>
<meta charset="utf-8">
<title>Le Ciel Stay – Apartments in Prague</title>
<link href="https://fonts.googleapis.com/css2?family=Ubuntu:wght@300;400;500;700&display=swap" rel="stylesheet">
<style>
:root{
  --teal:#12a08a;
  --teal-dark:#0d8a76;
  --brown:#8a4a2a;
  --orange:#d9781f;
  --olive:#8f9f3c;
  --copper:#b8732a;
  --ink:#2b2b2b;
  --muted:#6a6a6a;
  --footer:#333333;
  --panel:rgba(60,30,15,.82);
  --field:#7a4525;
}
*{margin:0;padding:0;box-sizing:border-box}
html,body{width:1200px;height:1200px;overflow:hidden;background:#ffffff}
body{font-family:'Ubuntu',sans-serif;color:var(--ink)}
.page{position:absolute;left:351px;top:0;width:611px;height:1475px;transform:scale(0.8136);transform-origin:0 0;background:#fff;overflow:hidden}
.a{position:absolute}
.c{text-align:center}

/* hero */
.hero{left:0;top:0;width:611px;height:272px;background:linear-gradient(180deg,#c98a55 0%,#d9893e 20%,#b8602a 35%,#5a3322 60%,#2a1c16 100%)}
.hero-top{left:0;top:0;width:611px;height:53px;background:linear-gradient(180deg,rgba(245,210,170,.85),rgba(230,170,110,.6))}
.topbar{font-size:5px;color:#4a2e1c;top:6px}
.brand{left:255px;top:12px;width:100px;display:flex;justify-content:center;align-items:center;gap:4px;color:#3a2517;font-size:8px;font-weight:500;letter-spacing:.5px}
.brand i{display:block;width:5px;height:5px;background:#3a2517}
.nav{top:42px;left:84px;width:450px;display:flex;justify-content:space-between;font-size:6px;color:#3a2517}
.nav span.sep{opacity:.6}
.tagline{left:204px;top:120px;width:198px;height:18px;background:#111;color:#fff;font-size:15px;line-height:18px;text-align:center;letter-spacing:.2px}
.booking{left:83px;top:176px;width:445px;height:85px;background:var(--panel)}
.lbl{font-size:5px;color:#f0e4da}
.field{background:var(--field);height:18px;font-size:5px;color:#f5ebe2;line-height:18px;padding-left:5px}
.btn-teal{background:var(--teal);color:#fff;font-size:6px;text-align:center}

/* about */
.about-h{left:75px;top:302px;font-size:17px;color:#333}
.about-name{left:72px;top:326px;font-size:40px;font-weight:300;color:var(--teal);line-height:46px}
.p5{font-size:5px;line-height:9.5px;color:#555}
ul.b5{list-style:none;font-size:5px;line-height:9.5px;color:#555}
ul.b5 li:before{content:"•";margin-right:4px}
.avatar{left:286px;top:381px;width:38px;height:38px;border-radius:50%;background:radial-gradient(circle at 50% 40%,#c9a88d,#6b7a52);border:2px solid #dfe6df}

/* properties */
.sec-title{left:0;width:611px;top:508px;font-size:11px;font-weight:500;text-align:center;color:#222}
.filters{left:190px;top:531px;width:230px;display:flex;justify-content:space-between;font-size:5px;font-weight:700;color:#333}
.filters .on{color:var(--orange)}
.photo{background:linear-gradient(160deg,#e9e2d6 0%,#cbb8a0 45%,#8c7360 70%,#5e5550 100%)}
.photo.green{background:linear-gradient(160deg,#e7e8e2 0%,#b4c0a3 35%,#6e7b4f 55%,#8a6a4c 80%,#4d3d30 100%)}
.photo.kitchen{background:linear-gradient(160deg,#f4f4f2 0%,#dfe2e4 40%,#b9a794 70%,#5a504c 100%)}
.card-title{font-size:9px;color:var(--brown);text-align:center;width:166px}
.card-addr{font-size:5px;color:#555;text-align:center;width:166px}
.feat{font-size:4.6px;color:#444;display:flex;justify-content:space-between;width:162px;align-items:center}
.feat span{display:flex;align-items:center;gap:2px}
.btn-out{border:1px solid #8a8a8a;font-size:6px;color:#444;text-align:center;line-height:18px;height:19px;width:77px}
.btn-book{background:var(--teal);font-size:6px;color:#fff;text-align:center;line-height:19px;height:19px;width:77px}
.need{left:397px;top:802px;width:166px;height:192px;background:var(--olive)}
.need-frame{left:9px;top:8px;width:148px;height:176px;border:1px solid rgba(255,255,255,.55)}
.wt{color:#fff}
.msg{left:397px;top:1006px;width:166px;height:19px;background:var(--copper);color:#fff;font-size:6px;line-height:19px;text-align:center}

/* promo */
.promo{left:0;top:1061px;width:611px;height:250px;background:linear-gradient(180deg,#2a3340 0%,#3a3534 50%,#5a3a26 75%,#2a2420 100%)}
.banner{width:165px;height:189px;top:1090px;overflow:hidden}
.b1{left:48px;background:#1f63b8}
.b2{left:223px;background:#e6e6e6}
.b3{left:399px;background:#f1d7c8}

/* footer */
.footer{left:0;top:1311px;width:611px;height:164px;background:var(--footer);color:#e8e8e8}
.f-h{font-size:6.5px;font-weight:700;color:#fff}
.f-list{list-style:none;font-size:5px;line-height:11.4px;color:#ddd}
.f-list li:before{content:"›";margin-right:4px}
.thumb{width:36px;height:36px;background:linear-gradient(160deg,#e8e2d8,#b9a690 55%,#6e5b4c)}
</style>
</head>
<body>
<div class="page">

  <!-- hero -->
  <div class="a hero" role="img" aria-label="Sunset skyline of the city with glowing towers"></div>
  <div class="a hero-top"></div>
  <div class="a topbar" style="left:55px">&#9742; 420 600 123 456 &nbsp;&nbsp;|&nbsp;&nbsp; &#9993; hello@lecielstay.cz</div>
  <div class="a brand"><i></i>Le Ciel Stay</div>
  <div class="a topbar" style="left:482px">&#9873; Discover Prague &nbsp;&nbsp;|&nbsp;&nbsp; EN &#9662;</div>
  <div class="a nav">
    <span>Apartments</span><span class="sep">|</span><span>Locations</span><span class="sep">|</span><span>Services</span><span class="sep">|</span><span>Gallery</span><span class="sep">|</span><span>News</span><span class="sep">|</span><span>Exclusive Offers &amp; Tours</span><span class="sep">|</span><span>For Families</span><span class="sep">|</span><span>Contact Us</span>
  </div>
  <div class="a tagline">BEING HOME IN PRAGUE</div>

  <svg class="a" style="left:0;top:0" width="611" height="272" aria-hidden="true">
    <defs><g id="pin"><path d="M5 0a5 5 0 0 1 5 5c0 4-5 8-5 8S0 9 0 5a5 5 0 0 1 5-5z" fill="#3cc3a8"/><circle cx="5" cy="5" r="2" fill="#fff"/></g></defs>
    <use href="#pin" x="78" y="111"/><use href="#pin" x="190" y="110"/><use href="#pin" x="259" y="98"/>
    <use href="#pin" x="252" y="142"/><use href="#pin" x="408" y="101"/><use href="#pin" x="467" y="111"/>
    <use href="#pin" x="536" y="96"/><use href="#pin" x="438" y="157"/><use href="#pin" x="589" y="188"/><use href="#pin" x="26" y="223"/>
  </svg>

  <div class="a booking">
    <div class="a lbl" style="left:14px;top:12px">Check In Date</div>
    <div class="a lbl" style="left:162px;top:12px">Check Out Date</div>
    <div class="a lbl" style="left:290px;top:12px">Adults</div>
    <div class="a lbl" style="left:334px;top:12px">Children</div>
    <div class="a lbl" style="left:377px;top:12px">Infants</div>
    <div class="a field" style="left:13px;top:22px;width:133px">11/12/2017</div>
    <div class="a field" style="left:150px;top:22px;width:134px">25/12/2017</div>
    <div class="a field" style="left:288px;top:22px;width:41px">2 <span style="float:right;margin-right:5px">&#8964;</span></div>
    <div class="a field" style="left:333px;top:22px;width:41px">0 <span style="float:right;margin-right:5px">&#8964;</span></div>
    <div class="a field" style="left:378px;top:22px;width:43px">0 <span style="float:right;margin-right:5px">&#8964;</span></div>
    <div class="a lbl" style="left:14px;top:54px">Promotional Code</div>
    <div class="a field" style="left:13px;top:64px;width:133px"></div>
    <div class="a btn-teal" style="left:150px;top:64px;width:134px;height:18px;line-height:18px">Check Availability</div>
    <div class="a" style="left:288px;top:64px;width:134px;height:18px;border:1px solid #7a4525"></div>
    <div class="a lbl" style="left:301px;top:70px;font-size:6px">or</div>
    <div class="a field" style="left:314px;top:67px;width:101px;height:12px;line-height:12px;font-size:4.5px">Select Rental unit <span style="float:right;margin-right:8px">&#8964;</span></div>
  </div>

  <!-- about -->
  <div class="a about-h">About</div>
  <div class="a about-name">Le Ciel</div>
  <p class="a p5" style="left:232px;top:300px;width:318px">Lorem ipsum dolor sit amet, consectetur adipiscing elit. Vestibulum iaculis eros sagittis, viverra elit a, congue turpis. Sed massa dui, tristique id blandit id, pellentesque sed libero. Aliquam ultricies eu arcu vitae interdum. Suspendisse maximus, massa sit amet laoreet egestas:</p>
  <ul class="a b5" style="left:232px;top:337px">
    <li>lorem lectus aliquam libero</li><li>convallis euismod odio orci a dolor</li><li>Consectetur adipiscing elit.</li>
  </ul>
  <ul class="a b5" style="left:366px;top:337px">
    <li>Quisque at neque ut justo egestas dictum eget et</li><li>Lorem ipsum dolor sit amet, consectetur adipiscing</li><li>Sed venenatis diam a sollicitudin blandit</li>
  </ul>

  <div class="a avatar" role="img" aria-label="Portrait of the company director"></div>
  <div class="a c" style="left:205px;top:425px;width:200px;font-size:7px;color:#333">JHON DOE.</div>
  <div class="a c" style="left:205px;top:435px;width:200px;font-size:5.5px;color:#555">Director, xyz company</div>
  <div class="a" style="left:95px;top:454px;font-size:9px;color:#555">&#8249;</div>
  <div class="a" style="left:496px;top:454px;font-size:9px;color:#555">&#8250;</div>
  <p class="a p5 c" style="left:130px;top:453px;width:350px">Lorem ipsum dolor sit amet, consectetur adipiscing elit. Vestibulum iaculis eros sagittis, viverra elit a, congue turpis. Sed massa dui, tristique id blandit id, pellentesque sed libero. Aliquam ultricies eu arcu vitae interdum. Suspendisse maximus, massa sit amet laoreet egestas, lorem lectus aliquam libero, convallis euismod odio orci a dolor. Quisque at neque ut justo egestas dictum eget et purus.</p>

  <!-- latest properties -->
  <div class="a sec-title">Latest Properties</div>
  <div class="a filters"><span class="on">All</span><span>|</span><span>Rent</span><span>|</span><span>Office</span><span>|</span><span>Apartment</span><span>|</span><span>Villa</span><span>|</span><span>Flat</span></div>

  <svg width="0" height="0" style="position:absolute">
    <defs>
      <g id="ibed"><rect x="0" y="2" width="8" height="3" fill="#333"/><rect x="0" y="0" width="3" height="2" fill="#333"/></g>
      <g id="ibath"><rect x="0" y="2" width="6" height="3" fill="none" stroke="#333" stroke-width=".8"/><line x1="1" y1="0" x2="1" y2="2" stroke="#333" stroke-width=".8"/></g>
      <g id="iuser"><circle cx="3" cy="1.6" r="1.6" fill="#333"/><path d="M0 6c0-2 1.3-3 3-3s3 1 3 3z" fill="#333"/></g>
    </defs>
  </svg>

  <!-- row 1 -->
  <div class="a photo" style="left:47px;top:554px;width:166px;height:158px" role="img" aria-label="Living room with grey sofa and tall windows"></div>
  <div class="a photo green" style="left:222px;top:554px;width:166px;height:158px" role="img" aria-label="Sitting room with armchairs and garden view"></div>
  <div class="a photo kitchen" style="left:397px;top:554px;width:166px;height:158px" role="img" aria-label="Open plan kitchen and lounge"></div>

  <div class="a card-title" style="left:47px;top:715px">New luxury Apaprtment</div>
  <div class="a card-title" style="left:222px;top:715px">New luxury Apaprtment</div>
  <div class="a card-title" style="left:397px;top:715px">New luxury Apaprtment</div>
  <div class="a card-addr" style="left:47px;top:728px">180, ABC Street, Prague</div>
  <div class="a card-addr" style="left:222px;top:728px">180, ABC Street, Prague</div>
  <div class="a card-addr" style="left:397px;top:728px">180, ABC Street, Prague</div>

  <div class="a feat" style="left:50px;top:740px"><span><svg width="8" height="5"><use href="#ibed"/></svg>3 Bedrooms</span><span><svg width="6" height="5"><use href="#ibath"/></svg>2 Bathrooms</span><span><svg width="6" height="6"><use href="#iuser"/></svg>Max. 4 Person</span></div>
  <div class="a feat" style="left:226px;top:740px"><span><svg width="8" height="5"><use href="#ibed"/></svg>3 Bedrooms</span><span><svg width="6" height="5"><use href="#ibath"/></svg>2 Bathrooms</span><span><svg width="6" height="6"><use href="#iuser"/></svg>Max. 2 Person</span></div>
  <div class="a feat" style="left:401px;top:740px"><span><svg width="8" height="5"><use href="#ibed"/></svg>3 Bedrooms</span><span><svg width="6" height="5"><use href="#ibath"/></svg>2 Bathrooms</span><span><svg width="6" height="6"><use href="#iuser"/></svg>Max. 4 Person</span></div>

  <div class="a btn-out" style="left:47px;top:759px">Details</div><div class="a btn-book" style="left:136px;top:759px">Book Now</div>
  <div class="a btn-out" style="left:223px;top:759px">Details</div><div class="a btn-book" style="left:311px;top:759px">Book Now</div>
  <div class="a btn-out" style="left:397px;top:759px">Details</div><div class="a btn-book" style="left:486px;top:759px">Book Now</div>

  <!-- row 2 -->
  <div class="a photo" style="left:47px;top:802px;width:166px;height:157px" role="img" aria-label="Living room with grey sofa and tall windows"></div>
  <div class="a photo green" style="left:222px;top:802px;width:166px;height:157px" role="img" aria-label="Sitting room with armchairs and garden view"></div>
  <div class="a card-title" style="left:47px;top:961px">New luxury Apaprtment</div>
  <div class="a card-title" style="left:222px;top:961px">New luxury Apaprtment</div>
  <div class="a card-addr" style="left:47px;top:975px">180, ABC Street, Prague</div>
  <div class="a card-addr" style="left:222px;top:975px">180, ABC Street, Prague</div>
  <div class="a feat" style="left:50px;top:987px"><span><svg width="8" height="5"><use href="#ibed"/></svg>3 Bedrooms</span><span><svg width="6" height="5"><use href="#ibath"/></svg>2 Bathrooms</span><span><svg width="6" height="6"><use href="#iuser"/></svg>Max. 2 Person</span></div>
  <div class="a feat" style="left:226px;top:987px"><span><svg width="8" height="5"><use href="#ibed"/></svg>3 Bedrooms</span><span><svg width="6" height="5"><use href="#ibath"/></svg>2 Bathrooms</span><span><svg width="6" height="6"><use href="#iuser"/></svg>Max. 5 Person</span></div>
  <div class="a btn-out" style="left:47px;top:1006px">Details</div><div class="a btn-book" style="left:136px;top:1006px">Book Now</div>
  <div class="a btn-out" style="left:223px;top:1006px">Details</div><div class="a btn-book" style="left:311px;top:1006px">Book Now</div>

  <!-- need to know -->
  <div class="a need">
    <div class="a need-frame"></div>
    <div class="a c wt" style="left:0;top:13px;width:166px;font-size:8.5px">Need To Know</div>
    <div class="a photo" style="left:9px;top:29px;width:148px;height:39px" role="img" aria-label="Apartment living room"></div>
    <div class="a c wt" style="left:0;top:73px;width:166px;font-size:5px">Apartments</div>
    <div class="a c wt" style="left:15px;top:82px;width:136px;font-size:4.6px;line-height:9.5px">Also available to rent all the apartments together for companies or larger groups.</div>
    <svg class="a" style="left:3px;top:91px" width="160" height="10" aria-hidden="true">
      <circle cx="5" cy="5" r="4.5" fill="#fff"/><path d="M6 3 4 5l2 2" stroke="var(--olive)" fill="none"/>
      <circle cx="155" cy="5" r="4.5" fill="#fff"/><path d="M154 3l2 2-2 2" stroke="var(--olive)" fill="none"/>
    </svg>
    <svg class="a" style="left:39px;top:112px" width="14" height="12" aria-hidden="true"><rect x="1" y="2" width="10" height="9" fill="none" stroke="#fff"/><line x1="1" y1="5" x2="11" y2="5" stroke="#fff"/><circle cx="10" cy="9" r="2.5" fill="var(--olive)" stroke="#fff"/></svg>
    <svg class="a" style="left:122px;top:112px" width="8" height="12" aria-hidden="true"><path d="M1 3 4 0l3 3v8H1z" fill="#fff"/><circle cx="4" cy="4" r="1" fill="var(--olive)"/></svg>
    <div class="a c wt" style="left:8px;top:130px;width:76px;font-size:5px">Check-Out</div>
    <div class="a c wt" style="left:8px;top:140px;width:76px;font-size:4.6px;line-height:9.5px">12 Noon. Earliest Check in 3 p.m. Both are flexible by arrangements.</div>
    <div class="a c wt" style="left:86px;top:130px;width:76px;font-size:5px">Rates</div>
    <div class="a c wt" style="left:89px;top:140px;width:70px;font-size:4.6px;line-height:9.5px">Price from 150 USD per night, including tax.</div>
  </div>
  <div class="a msg">&#9998;&nbsp;&nbsp; Please Leave A Message</div>

  <!-- promo banners -->
  <div class="a promo" role="img" aria-label="Night view of the old town skyline"></div>

  <div class="a banner b1">
    <div class="a" style="left:60px;top:0;width:120px;height:189px;background:linear-gradient(160deg,#eef0f2,#c9ccd0 60%,#9aa0a6);clip-path:polygon(35% 0,100% 0,100% 100%,0 100%,30% 60%,60% 20%)" role="img" aria-label="Bright bedroom with white linen"></div>
    <div class="a c" style="left:6px;top:44px;width:95px;font-size:11px;color:#fff;line-height:12px">Rent a condo<br>&amp;<br><b style="font-weight:500;font-size:10px">win exciting offers</b></div>
    <div class="a" style="left:28px;top:99px;width:72px;height:72px;border-radius:50%;background:var(--orange);color:#fff;font-size:10px;font-weight:700;text-align:center;line-height:13px;padding-top:23px">ENQUIRE<br>NOW!</div>
    <div class="a" style="left:4px;top:175px;font-size:3.5px;color:#fff">*T&amp;C Applied</div>
  </div>

  <div class="a banner b2">
    <div class="a" style="left:55px;top:0;width:110px;height:130px;background:linear-gradient(170deg,#6b5a4a,#b9915e 50%,#3c2e26);clip-path:polygon(30% 0,100% 0,100% 100%,0 45%)" role="img" aria-label="Historic street at dusk"></div>
    <svg class="a" style="left:112px;top:126px" width="40" height="24" aria-hidden="true"><path d="M0 0h40L20 24z" fill="#1a1a1a"/></svg>
    <div class="a" style="left:8px;top:92px;font-size:5px;letter-spacing:1.2px;color:#555">READY FLAT</div>
    <div class="a" style="left:8px;top:100px;font-size:9px;font-weight:500;color:var(--orange)">FOR SALE</div>
    <div class="a" style="left:8px;top:114px;font-size:17px;line-height:22px;color:#333">Luxurious<br>Apartment<br>in Prague</div>
  </div>

  <div class="a banner b3">
    <div class="a" style="left:6px;top:68px;width:120px;height:118px;background:radial-gradient(ellipse at 50% 55%,#ffffff 0%,#d6d6d6 45%,#8f8f8f 60%,rgba(241,215,200,0) 72%)" role="img" aria-label="Model house on a wooden floor"></div>
    <div class="a" style="right:5px;top:5px;font-size:5px;letter-spacing:1.4px;color:#444;text-align:right">TIPS BEFORE</div>
    <div class="a" style="right:5px;top:13px;font-size:8.5px;font-weight:500;color:var(--orange);text-align:right">RENTING AND BUYING</div>
    <div class="a" style="right:5px;top:27px;font-size:17px;line-height:23px;color:#333;text-align:right">An Apartment<br>in Prague</div>
  </div>

  <!-- footer -->
  <div class="a footer">
    <div class="a f-h" style="left:53px;top:21px">About LeCielStay.cz</div>
    <p class="a" style="left:52px;top:34px;width:165px;font-size:4.8px;line-height:9.6px;color:#ddd">Lorem ipsum dolor sit amet, consectetur adipiscing elit. Vestibulum iaculis eros sagittis, viverra elit a, congue turpis. Sed massa dui, tristique id blandit id, pellentesque sed libero. Aliquam ultricies eu arcu vitae interdum. Suspendisse maximus, massa sit amet laoreet egestas, lorem lectus aliquam libero.</p>
    <svg class="a" style="left:52px;top:96px" width="90" height="8" aria-hidden="true">
      <circle cx="3" cy="4" r="3" fill="#fff"/><line x1="14" y1="0" x2="14" y2="8" stroke="#777" stroke-width=".6"/>
      <circle cx="27" cy="4" r="3" fill="#fff"/><line x1="39" y1="0" x2="39" y2="8" stroke="#777" stroke-width=".6"/>
      <circle cx="54" cy="4" r="3" fill="#fff"/><line x1="66" y1="0" x2="66" y2="8" stroke="#777" stroke-width=".6"/>
      <circle cx="81" cy="4" r="3" fill="#fff"/>
    </svg>

    <div class="a f-h" style="left:268px;top:21px">Quick Link</div>
    <ul class="a f-list" style="left:264px;top:32px">
      <li>Apartments</li><li>Locations</li><li>Services</li><li>Gallery</li><li>News</li><li>Exclusive Offers &amp; Tours</li><li>For Families</li><li>Contact Us</li>
    </ul>
    <div class="a f-h" style="left:358px;top:21px">Quick Link 2</div>
    <ul class="a f-list" style="left:354px;top:32px">
      <li>Terms And Conditions</li><li>Privacy Policy</li><li>Aggrements</li><li>Sellers</li><li>Testimonials</li><li>Reviews &amp; ratings</li>
    </ul>
    <div class="a f-h" style="left:446px;top:21px">Gallery</div>
    <div class="a thumb" style="left:446px;top:30px" role="img" aria-label="Apartment interior"></div>
    <div class="a thumb" style="left:486px;top:30px" role="img" aria-label="Apartment interior"></div>
    <div class="a thumb" style="left:526px;top:30px" role="img" aria-label="Apartment interior"></div>
    <div class="a thumb" style="left:446px;top:70px" role="img" aria-label="Apartment interior"></div>
    <div class="a thumb" style="left:486px;top:70px" role="img" aria-label="Apartment interior"></div>
    <div class="a thumb" style="left:526px;top:70px" role="img" aria-label="Apartment interior"></div>

    <div class="a" style="left:48px;top:137px;width:515px;height:1px;background:#666"></div>
    <div class="a" style="left:53px;top:147px;font-size:5px;color:#ddd">&copy; 2017 Le Ciel Stay. All Rights Reserved</div>
  </div>

</div>
</body>
</html>
```